Learn-to-Swim Program for Children's Day Camp (Walter Brightley Fieldgrounds)

We are a children's camp with a robust swim instruction program and we need a series of 5 kid-friendly banners which list the skills learned in our swim program that can be hung up around each outdoor pool complex. All together there are 6 overarching levels and 12 sublevels (see attached). Except for the Level V & VI, each banner should be one overarching level and the 2-3 sublevels that define it.

Each swim level has a name, most of which are sea creatures, and we want to have a corresponding image/avatar to go with the swim level name (e.g. tadpole, barracuda, orca, goldfish, catfish).

The banners should be 3 feet (width) by 5 feet (height). The banners will be hung outdoors so it needs a color scheme that won't get lost in the sunlight.

We will want to include our logo but do not need the design to match our logo colors. Logo can be in black or white.

Our website is: www.campwbf.example

Target Market(s)

children age 5 - 12

Industry/Entity Type

children's day camp

Requirements
Must have
• A progression from level I to level VI. Should have a happy, bright, fun, tone, text MUST be legible from at least a 5 foot distance
Should not have
• adult themes, a scheme that evokes sadness or fear

```html
<!DOCTYPE html>
<html lang="en">
<head>
<meta charset="utf-8">
<title>ARC II – Swim Levels – Walter Brightley Fieldgrounds</title>
<link rel="stylesheet" href="https://fonts.googleapis.com/css2?family=Fredoka:wght@600;700&family=Fira+Sans:wght@500&family=Fira+Sans+Condensed:wght@500&display=swap">
<style>
  :root {
    --header-teal: #50b3a5;
    --header-strip: #6cbdb6;
    --title-green: #2fb56c;
    --title-dark: #0c6b36;
    --water-top: #c8e7f2;
    --water-mid: #72c4e8;
    --water-bottom: #4d6fb8;
    --ink-blue: #1a6fbe;
    --label-blue: #1565c0;
    --white: #ffffff;
    --fish-a: #6b2450;
    --fish-b: #9cc7e0;
    --tadpole-a: #4c5566;
    --tadpole-b: #e9ecc8;
  }
  * { box-sizing: border-box; margin: 0; padding: 0; }
  html, body { width: 720px; height: 1200px; overflow: hidden; }
  body { font-family: "Fira Sans", sans-serif; }

  .banner {
    position: relative;
    width: 720px;
    height: 1200px;
    background: linear-gradient(to bottom, var(--water-top) 130px, var(--water-mid) 640px, var(--water-bottom) 1200px);
    overflow: hidden;
  }
  .banner-header {
    position: absolute; inset: 0 0 auto 0;
    height: 130px;
    background: var(--header-teal);
    border-bottom: 10px solid var(--header-strip);
    display: flex; justify-content: center; align-items: center;
  }
  .banner-title {
    font-family: "Fredoka", sans-serif;
    font-weight: 700;
    font-size: 96px;
    line-height: 1;
    letter-spacing: -2px;
    color: var(--title-green);
    -webkit-text-stroke: 12px var(--title-dark);
    paint-order: stroke fill;
    position: relative;
    top: -4px;
  }

  .outlined {
    font-family: "Fredoka", sans-serif;
    font-weight: 700;
    color: var(--white);
    -webkit-text-stroke: 7px var(--label-blue);
    paint-order: stroke fill;
    position: absolute;
    line-height: 1;
    white-space: nowrap;
  }
  .level-word { font-size: 36px; font-weight: 600; }
  .level-name { font-size: 62px; letter-spacing: 1px; }
  .skills-label { font-size: 36px; font-weight: 600; }
  .moveup-label { font-size: 46px; letter-spacing: -1px; }

  .skills-box {
    position: absolute;
    left: 336px; width: 358px;
    border: 5px solid var(--ink-blue);
    border-bottom: none;
    border-radius: 0 26px 0 0;
  }
  .skills-box.light { border-color: var(--white); }
  .skills-list {
    list-style: none;
    padding: 0 6px 0 51px;
    color: var(--ink-blue);
    font-size: 18px;
    line-height: 22px;
  }
  .skills-list li { position: relative; }
  .skills-list li::before {
    content: "";
    position: absolute;
    left: -24px; top: 9px;
    width: 5px; height: 5px;
    border-radius: 50%;
    background: var(--ink-blue);
  }
  .level-tadpole .skills-list {
    color: var(--white);
    font-family: "Fira Sans Condensed", sans-serif;
    font-size: 19px;
  }
  .level-tadpole .skills-list li::before { background: var(--white); }

  .moveup-box {
    position: absolute;
    left: 195px; width: 499px;
    background: var(--white);
    border: 5px solid var(--ink-blue);
    border-radius: 30px;
    padding: 10px 8px 0 25px;
    color: var(--ink-blue);
    font-size: 18px;
    line-height: 23px;
    letter-spacing: -0.2px;
  }
  .level-tadpole .moveup-box {
    border: none;
    font-family: "Fira Sans Condensed", sans-serif;
    font-size: 19px;
    letter-spacing: -0.3px;
    padding: 14px 8px 0 27px;
  }

  .avatar { position: absolute; }
  .avatar-guppy {
    left: 45px; top: 240px; width: 250px; height: 260px;
    border-radius: 50% 40% 45% 50%;
    background: radial-gradient(ellipse at 60% 55%, var(--fish-a), var(--fish-b) 80%, transparent 100%);
    opacity: .8;
  }
  .avatar-tadpole {
    left: 55px; top: 805px; width: 215px; height: 175px;
    border-radius: 50%;
    background: radial-gradient(ellipse at 65% 65%, var(--tadpole-a) 45%, var(--tadpole-b) 90%, transparent 100%);
    opacity: .85;
  }

  .camp-mark {
    position: absolute;
    left: 0; right: 0; top: 1166px;
    display: flex; justify-content: center; align-items: center; gap: 6px;
    font-size: 14px;
    color: #8fb5e0;
    letter-spacing: 1px;
  }
  .camp-mark i { display: block; width: 10px; height: 10px; background: #8fb5e0; }
</style>
</head>
<body>
<main class="banner">
  <header class="banner-header">
    <h1 class="banner-title">ARC II</h1>
  </header>

  <section class="level level-guppy">
    <div class="outlined level-word" style="left:32px; top:146px;">Level</div>
    <h2 class="outlined level-name" style="left:32px; top:184px;">GUPPY</h2>
    <div class="avatar avatar-guppy" role="img" aria-label="Illustration of a purple guppy fish swimming"></div>

    <div class="skills-box" style="top:172px; height:372px;">
      <ul class="skills-list" style="margin-top:28px;">
        <li>Fully submerges and retrieves<br>object from under water</li>
        <li>Blows bubbles through nose and<br>mouth</li>
        <li>Floats on stomach with support<br>(10 seconds) Floats on back with<br>support (10 seconds)</li>
        <li>Assisted glide on stomach- no<br>kicking</li>
        <li>Rolls from front to back and back<br>to front with support</li>
        <li>Straight leg flutter kick on front<br>and back (15 seconds) with<br>support</li>
      </ul>
    </div>
    <div class="outlined skills-label" style="left:337px; top:148px;">Skills</div>

    <div class="moveup-box" style="top:544px; height:72px;">
      Must demonstrate straight flutter kicks and float with<br>support
    </div>
    <div class="outlined moveup-label" style="left:24px; top:556px;">Move-Up</div>
  </section>

  <section class="level level-tadpole">
    <div class="outlined level-word" style="left:32px; top:652px;">Level</div>
    <h2 class="outlined level-name" style="left:32px; top:694px;">TADPOLE</h2>
    <div class="avatar avatar-tadpole" role="img" aria-label="Illustration of a smiling grey tadpole"></div>

    <div class="skills-box light" style="top:674px; height:374px;">
      <ul class="skills-list" style="margin-top:35px;">
        <li>Floats on back unsupported (10<br>sec)</li>
        <li>Floats on stomach unsupported (10<br>sec)</li>
        <li>Launch glide on stomach with<br>proper flutter kick unassisted</li>
        <li>Launch glide on back with proper<br>flutter kick unassisted</li>
        <li>Push off and swim using<br>combination of arm and leg actions<br>for 10 feet on front and back</li>
        <li>Launch-roll to back float<br>unsupported</li>
        <li>Jump in and float on the back</li>
      </ul>
    </div>
    <div class="outlined skills-label" style="left:337px; top:654px;">Skills</div>

    <div class="moveup-box" style="top:1048px; height:77px;">
      Must perform proper flutter kicks and glides unsupported.<br>Must jump in and float on the back for 10 sec.
    </div>
    <div class="outlined moveup-label" style="left:26px; top:1062px;">Move-Up</div>
  </section>

  <footer class="camp-mark" aria-label="Walter Brightley Fieldgrounds">
    <span>WBF</span><i></i>
  </footer>
</main>
</body>
</html>
```